Stationery for Family Law Attorney
Business Cards, Envelope, Letterhead
Stationery for Family Law Attorney - Law
Creative Brief
Professional
Marisol K. Denby
Attorney & Counselor at Law
27815 E. Halvorsen Lane Suite 300 San Diego, CA 92984
marisol@counseldenby.example
Exclusively Family Law www.counseldenby.example
MDenby MDenby
Please note the address should read as follows, on the following lines: Line 1: The Quillgate Line 2: 27815 E. Halvorsen Lane Line 3: Suite 610 Line 4: San Diego, CA 92984
Please note the "San Diego, CA 92984" needs to all be on the same line. (858) 555-0147 is the fax line - not the cell. Also, please add the words "The Quillgate" on the line above the 27815 E. Halvorsen Lane line.
Vektor Vektor
sir please check you inbox top right side this web page
Re #37: Please make the back gray. Please replace the symbols with the words for the contact information (i.e. "Phone"). Please remove the website from the front.
Re #30: Please make the "Marisol K. Denby" and "Attorney & Counselor at Law part in small and large caps. Please remove the website from the front of the card. Instead of letters, please write out "Phone" "Fax" and "Email". Thanks. I really like the gray back of the card.

```html
<!DOCTYPE html>
<html lang="en">
<head>
<meta charset="utf-8">
<title>Marisol K. Denby — Stationery</title>
<link href="https://fonts.googleapis.com/css2?family=Cinzel:wght@400;600&family=Open+Sans:wght@400;600;700&display=swap" rel="stylesheet">
<style>
:root{
  --backdrop:#e8e5e0;
  --paper:#ffffff;
  --navy:#1f3552;
  --blue:#2a6aa8;
  --sky:#5fa3d6;
  --ink:#2b2b2b;
  --muted:#7b8591;
  --line:#b9c1ca;
  --card-back:#e6eaee;
}
*{box-sizing:border-box;margin:0;padding:0}
html,body{width:1200px;height:557px;overflow:hidden;background:var(--backdrop)}
body{position:relative;font-family:"Open Sans",sans-serif;color:var(--ink)}
.sheet,.card,.envelope{position:absolute;background:var(--paper);box-shadow:0 2px 6px rgba(0,0,0,.18)}
.sheet{top:34px;width:366px;height:500px}
.fax-sheet{left:29px}
.letterhead{left:408px}

.masthead{text-align:center;color:var(--navy)}
.masthead .mark{display:block;margin:0 auto 3px;background:var(--navy)}
.masthead .pre{font-family:"Cinzel",serif;font-size:6px;letter-spacing:1px}
.masthead .name{font-family:"Cinzel",serif;font-weight:600;line-height:1}
.masthead .post{font-family:"Cinzel",serif;font-size:5px;letter-spacing:1px;margin-top:2px}
.sheet .masthead{padding-top:20px}
.sheet .mark{width:26px;height:18px}
.sheet .name{font-size:17px;letter-spacing:.5px}

.fax-title{position:absolute;right:22px;top:78px;font-weight:700;font-size:14px;letter-spacing:1px}
.fax-fields{position:absolute;left:22px;right:22px;top:98px;display:grid;grid-template-columns:1fr 1fr;column-gap:10px;border-top:1px solid var(--line)}
.fax-fields div{font-size:6.5px;padding:5px 0 3px;border-bottom:1px solid var(--line)}
.fax-options{position:absolute;left:22px;right:22px;top:172px;display:flex;justify-content:space-between;font-size:6px}
.fax-options span::before{content:"";display:inline-block;width:6px;height:6px;border:1px solid var(--muted);margin-right:3px;vertical-align:-1px}

.sheet-footer{position:absolute;left:0;right:0;bottom:0}
.sheet-footer .contact{text-align:center;font-size:4.5px;color:var(--muted);padding:0 10px 4px}
.sheet-footer .rule{height:2px;background:var(--sky)}
.sheet-footer .band{height:14px;background:var(--navy);color:#cfe1f2;font-family:"Cinzel",serif;font-size:7px;letter-spacing:5px;text-align:center;line-height:14px}

.card{top:36px;width:190px;height:112px}
.card-front{left:803px}
.card-front .masthead{padding-top:14px}
.card-front .mark{width:16px;height:11px}
.card-front .name{font-size:10px}
.card-front .details{position:absolute;left:0;right:0;bottom:8px;text-align:center;font-size:4.2px;color:var(--muted);line-height:1.5}
.card-front .band{position:absolute;left:0;right:0;bottom:0;height:4px;background:var(--navy)}
.card-back{left:1003px;background:var(--card-back);display:flex;align-items:center;justify-content:center}
.card-back p{font-family:"Cinzel",serif;font-size:7px;letter-spacing:2px;color:var(--blue)}

.envelope{left:800px;width:390px}
.envelope-back{top:246px;height:134px;overflow:hidden}
.envelope-back .flap{position:absolute;left:0;right:0;top:0;height:52px;background:linear-gradient(180deg,#2d5a86,#1f3552)}
.envelope-back .masthead{position:absolute;left:0;right:0;top:10px;color:#fff}
.envelope-back .mark{width:14px;height:10px;background:#fff}
.envelope-back .name{font-size:11px}
.envelope-back .fold{position:absolute;inset:0}

.envelope-front{top:424px;height:124px}
.envelope-front .masthead{position:absolute;left:14px;top:12px;width:130px}
.envelope-front .mark{width:14px;height:10px}
.envelope-front .name{font-size:9px}
.envelope-front .return{position:absolute;left:14px;top:52px;width:130px;text-align:center;font-size:4.5px;color:var(--muted);line-height:1.5}
.envelope-front .band{position:absolute;left:0;right:0;bottom:0;height:5px;background:var(--navy);border-top:1px solid var(--sky)}
</style>
</head>
<body>

<section class="sheet fax-sheet">
  <header class="masthead">
    <span class="mark"></span>
    <p class="pre">Law Offices of</p>
    <p class="name">Marisol K. Denby</p>
    <p class="post">A Professional Corporation</p>
  </header>
  <h1 class="fax-title">FAX</h1>
  <div class="fax-fields">
    <div>To :</div><div>From :</div>
    <div>Fax :</div><div>pages :</div>
    <div>Phone :</div><div>date :</div>
    <div>Re :</div><div>CC :</div>
  </div>
  <div class="fax-options">
    <span>Urgent</span><span>For Review</span><span>Please Comment</span><span>Please Reply</span><span>Please Recycle</span>
  </div>
  <footer class="sheet-footer">
    <p class="contact">The Quillgate · 27815 E. Halvorsen Lane · Suite 610 · San Diego, CA 92984 · Fax (858) 555-0147 · marisol@counseldenby.example</p>
    <div class="rule"></div>
    <div class="band">Exclusively Family Law</div>
  </footer>
</section>

<section class="sheet letterhead">
  <header class="masthead">
    <span class="mark"></span>
    <p class="pre">Law Offices of</p>
    <p class="name">Marisol K. Denby</p>
    <p class="post">A Professional Corporation</p>
  </header>
  <footer class="sheet-footer">
    <p class="contact">The Quillgate · 27815 E. Halvorsen Lane · Suite 610 · San Diego, CA 92984 · Fax (858) 555-0147 · marisol@counseldenby.example</p>
    <div class="rule"></div>
    <div class="band">Exclusively Family Law</div>
  </footer>
</section>

<section class="card card-front">
  <header class="masthead">
    <span class="mark"></span>
    <p class="pre">Law Offices of</p>
    <p class="name">Marisol K. Denby</p>
    <p class="post">Attorney &amp; Counselor at Law</p>
  </header>
  <div class="details">
    <p>The Quillgate · 27815 E. Halvorsen Lane · Suite 610</p>
    <p>San Diego, CA 92984 · Fax (858) 555-0147</p>
  </div>
  <div class="band"></div>
</section>

<section class="card card-back">
  <p>Exclusively Family Law</p>
</section>

<section class="envelope envelope-back">
  <svg class="fold" viewBox="0 0 390 134" preserveAspectRatio="none" aria-hidden="true">
    <path d="M0 52 L195 96 L390 52" fill="none" stroke="#d6dde4" stroke-width="1"/>
  </svg>
  <div class="flap"></div>
  <header class="masthead">
    <span class="mark"></span>
    <p class="name">Marisol K. Denby</p>
  </header>
</section>

<section class="envelope envelope-front">
  <header class="masthead">
    <span class="mark"></span>
    <p class="pre">Law Offices of</p>
    <p class="name">Marisol K. Denby</p>
  </header>
  <div class="return">
    <p>The Quillgate</p>
    <p>27815 E. Halvorsen Lane</p>
    <p>Suite 610</p>
    <p>San Diego, CA 92984</p>
  </div>
  <div class="band"></div>
</section>

</body>
</html>
```